Tor Ridge Wine Club-The Onyx Roll

We are a new aspirational brand of fine Tasmania Wine. We need a commitment club poster which appeals to the ego.We have one opportunity to get customers to sign up and that is when they visit at the cellar door. This club is the core of our business.

The brand is a clean, pure , simple brand, black and white very sophiscated.
This is a top end product.

Our Commitment Club is named The Onyx Roll which is a play on words. Tradionally The Onyx Roll is a list of people that you dont want to do business with. So we are turning this on its had.

You need to make this poster sharp, desirable, possibly sexy but masculine. Im thinking Felix Crane . It doesnt matter the client will be 40 up fashion consious looking for something new , exclusive , something there peers don't have.

I dont like busy! make it clean clear and basically undeniable. The client must not be able to resist the offer.

www.torridgevines.com.au

Reason: Internet problems so cant get to respond and offer comment in a timely manner

Appreciator 40-60 male wants to be recognised fashion consious sophiscated has money and wants to part of something exclusive.

A feeling that you are part of something that only a few are. Exclusive

Maybe an imagine of beautiful people 30/40ish I want to be drinking Tor Wine / in The Onyx Roll

Fashion

Must have
• Tor Ridge Logo
TOR Bottles images

We produce only 1600 cases of wine each vintage. Therefore we have limited membership 001-999 for our club.
Award Winning Wines available exclusively from us.

Gold Member
We will reserve 2 cases of our limited vintage, to be delivered to you in May and Oct.
Single varietal or mixed cases. You receive a 15% discount.

Silver Member
We will reserve 1 case of our limited vintage to be delivered to you 6 bottles in May and 6 in Oct.
Single varietal or mixed cases. You receive a 10% discount.

To you exclusively from us not, available from any other retailers.

You will be invited to Onyx Roll Only Events and Tastings.
You will get preferential access to new and limited releases.
Members will be entered in a bi annual draw to win a 2 night stay here at the Tor Weavers Cottage on the Freycinet Coast Tasmania.

• VIP stamps,gimacs, anything that cheapens our brand.

We do not like busy posters please have white space

```html
<!DOCTYPE html>
<html lang="en">
<head>
<meta charset="utf-8">
<title>Tor Ridge – Join the Onyx Roll</title>
<link rel="stylesheet" href="https://fonts.googleapis.com/css2?family=Cormorant+SC:wght@400;500&family=Pinyon+Script&display=swap">
<style>
  :root {
    --bg-top: #232323;
    --bg-bottom: #1a1a1a;
    --ink-white: #f2f2f2;
    --ink-soft: #d8d8d8;
    --gold-light: #f0cf6a;
    --gold: #c99a2e;
    --gold-deep: #8a6418;
    --silver-light: #ffffff;
    --silver: #b9b9b9;
    --silver-deep: #6e6e6e;
    --satin-light: #8a8a8a;
    --satin-dark: #2a2a2a;
  }
  html, body {
    margin: 0;
    padding: 0;
    width: 865px;
    height: 1200px;
    overflow: hidden;
    background: var(--bg-bottom);
  }
  .poster {
    position: relative;
    width: 865px;
    height: 1200px;
    overflow: hidden;
    background: linear-gradient(180deg, var(--bg-top) 0%, var(--bg-bottom) 100%);
    font-family: "Cormorant SC", "Times New Roman", serif;
    color: var(--ink-white);
  }
  .line {
    position: absolute;
    left: 0;
    right: 0;
    margin: 0;
    text-align: center;
    white-space: nowrap;
  }
  .bow-tie {
    position: absolute;
    left: 210px;
    top: 67px;
    width: 446px;
    height: 232px;
  }
  .brand {
    top: 268px;
    font-size: 40px;
    line-height: 50px;
    font-weight: 500;
    letter-spacing: 2px;
    color: var(--ink-white);
  }
  .invite {
    top: 372px;
    font-size: 13px;
    line-height: 16px;
    letter-spacing: 4px;
    color: var(--ink-soft);
  }
  .script {
    font-family: "Pinyon Script", "Brush Script MT", cursive;
    font-weight: 400;
  }
  .headline {
    top: 425px;
    font-size: 64px;
    line-height: 84px;
    background: linear-gradient(180deg, var(--gold-light) 0%, var(--gold) 55%, var(--gold-deep) 100%);
    -webkit-background-clip: text;
    background-clip: text;
    color: transparent;
  }
  .flourish {
    position: absolute;
    left: 387px;
    width: 92px;
    height: 22px;
  }
  .flourish--upper { top: 519px; }
  .flourish--lower { top: 971px; }
  .levels {
    top: 566px;
    font-size: 22px;
    line-height: 26px;
    letter-spacing: 5px;
    color: var(--ink-white);
  }
  .tier-title {
    font-size: 58px;
    line-height: 76px;
    -webkit-background-clip: text;
    background-clip: text;
    color: transparent;
  }
  .tier-title--gold {
    top: 628px;
    background-image: linear-gradient(180deg, var(--gold-light) 0%, var(--gold) 55%, var(--gold-deep) 100%);
  }
  .tier-title--silver {
    top: 787px;
    background-image: linear-gradient(180deg, var(--silver-light) 0%, var(--silver) 50%, var(--silver-deep) 100%);
  }
  .tier-detail {
    font-size: 17px;
    line-height: 20px;
    letter-spacing: 1px;
  }
  .tier-detail--gold { color: var(--gold); }
  .tier-detail--gold.first { top: 710px; }
  .tier-detail--gold.second { top: 741px; }
  .tier-detail--silver { color: var(--ink-soft); }
  .tier-detail--silver.first { top: 875px; }
  .tier-detail--silver.second { top: 907px; }
  .perk {
    font-size: 13.5px;
    line-height: 16px;
    letter-spacing: 0.6px;
    color: var(--ink-white);
  }
  .perk.one { top: 1030px; }
  .perk.two { top: 1058px; }
  .perk.three { top: 1086px; }
</style>
</head>
<body>
<main class="poster">
  <svg class="bow-tie" viewBox="0 0 446 232" role="img" aria-label="Illustration of a black satin bow tie">
    <defs>
      <linearGradient id="satin" x1="0" y1="0" x2="0" y2="1">
        <stop offset="0" stop-color="var(--satin-light)"/>
        <stop offset="1" stop-color="var(--satin-dark)"/>
      </linearGradient>
    </defs>
    <rect x="0" y="0" width="446" height="232" rx="40" fill="url(#satin)"/>
  </svg>

  <p class="line brand">Tor Ridge</p>

  <p class="line invite">invites you to</p>

  <h1 class="line script headline">Join the Onyx Roll</h1>

  <svg class="flourish flourish--upper" viewBox="0 0 92 22" role="img" aria-label="Small gold ornamental flourish">
    <rect x="0" y="0" width="92" height="22" rx="11" fill="var(--gold)"/>
  </svg>

  <h2 class="line levels">Two levels of commitment</h2>

  <h3 class="line script tier-title tier-title--gold">Gold Membership</h3>
  <p class="line tier-detail tier-detail--gold first">Reserve 2 cases of Wine delivered to you</p>
  <p class="line tier-detail tier-detail--gold second">1 May 1 Oct You choose the variety 15% DISCOUNT</p>

  <h3 class="line script tier-title tier-title--silver">Silver Membership</h3>
  <p class="line tier-detail tier-detail--silver first">Reserve 1/2 case of your choice of wine delivered</p>
  <p class="line tier-detail tier-detail--silver second">to you 1 May 1 Oct you choose your variety 10% DISCOUNT</p>

  <svg class="flourish flourish--lower" viewBox="0 0 92 22" role="img" aria-label="Small gold ornamental flourish">
    <rect x="0" y="0" width="92" height="22" rx="11" fill="var(--gold)"/>
  </svg>

  <p class="line perk one">Not available with other retailers Exclusively to you from us.</p>
  <p class="line perk two">Preferential access to first releases and limited releases</p>
  <p class="line perk three">VIP access to Onyx Roll only tastings and events.</p>
</main>
</body>
</html>
```